REAL PSYCHIC rear window decal. Mystical, light, positive, spiritual coach vibes

Design a sign for my back car window.
HOT PINK and purple swirly, mystical sign. Eye-catching and classy.
Size 24” x 18”
TEXT:
MARISOL DEANE
Psychic & Medium
Www,.marisoldeane.com
World Renowned for Over 45 Years. (This last line make small at bottom)

*This is not a filled in magnet, it will be transparent.

Target Market(s)

Women

Industry/Entity Type

Spirituality

Font styles to use
Script
Other font styles liked:
• See upload for a font I like

Colors
E54698
E96AAD
F1A4CE
F9D9EA
FCEFF6
A7469A
B969AE
D3A5CF
EDDBEB
F8F0F9
6B429C
8869AF
B7A5CE
E3DAEB
F3F0F8

Requirements
Must have
• Pink purple, classy yet mystical vibe
Nice to have
• Easy to read, but old-timey classic font for “MARISOL DEANE”

```html
<!DOCTYPE html>
<html lang="en">
<head>
<meta charset="utf-8">
<title>Marisol Deane — Psychic &amp; Medium Rear Window Decal</title>
<link rel="stylesheet" href="https://fonts.googleapis.com/css2?family=Pinyon+Script&family=Poppins:wght@500;600;700&display=swap">
<style>
  :root {
    --page-navy: #22406f;
    --burst-center: #b23aa6;
    --burst-mid: #941f89;
    --burst-edge: #701565;
    --ink-white: #ffffff;
    --amp-purple: #8e1d84;
  }
  html, body {
    margin: 0;
    padding: 0;
    width: 1042px;
    height: 1200px;
    overflow: hidden;
    background: var(--page-navy);
  }
  .canvas {
    position: relative;
    width: 1042px;
    height: 1200px;
  }
  .decal {
    position: absolute;
    left: 51px;
    top: 247px;
    width: 940px;
    height: 705px;
    display: block;
  }
  .decal__name {
    font-family: "Pinyon Script", cursive;
    font-size: 132px;
    fill: var(--ink-white);
  }
  .decal__title {
    font-family: "Poppins", sans-serif;
    font-weight: 700;
    font-size: 94px;
    fill: var(--ink-white);
  }
  .decal__amp {
    font-family: "Poppins", sans-serif;
    font-weight: 700;
    font-size: 50px;
    fill: var(--amp-purple);
  }
  .decal__url {
    font-family: "Poppins", sans-serif;
    font-weight: 600;
    font-size: 52px;
    fill: var(--ink-white);
  }
  .decal__url-frame {
    fill: none;
    stroke: var(--ink-white);
    stroke-width: 3;
  }
  .decal__tagline {
    font-family: "Poppins", sans-serif;
    font-weight: 500;
    font-size: 25px;
    fill: var(--ink-white);
  }
</style>
</head>
<body>
<main class="canvas">
  <svg class="decal" viewBox="0 0 940 705" xmlns="http://www.w3.org/2000/svg">
    <defs>
      <radialGradient id="burstGlow" cx="50%" cy="52%" r="70%">
        <stop offset="0%" stop-color="var(--burst-center)"/>
        <stop offset="45%" stop-color="var(--burst-mid)"/>
        <stop offset="100%" stop-color="var(--burst-edge)"/>
      </radialGradient>
    </defs>

    <rect class="decal__backdrop" x="0" y="0" width="940" height="705" fill="url(#burstGlow)"
          role="img" aria-label="Radiating magenta light-burst pattern backdrop"/>

    <text class="decal__name" x="470" y="244" text-anchor="middle"
          textLength="812" lengthAdjust="spacingAndGlyphs">Marisol Deane</text>

    <text class="decal__title" x="469" y="366" text-anchor="middle"
          textLength="378" lengthAdjust="spacingAndGlyphs">PSYCHIC</text>

    <g class="decal__amp-badge">
      <circle cx="290" cy="430" r="35" fill="var(--ink-white)"/>
      <text class="decal__amp" x="290" y="448" text-anchor="middle">&amp;</text>
    </g>
    <text class="decal__title" x="337" y="462"
          textLength="328" lengthAdjust="spacingAndGlyphs">MEDIUM</text>

    <rect class="decal__url-frame" x="117" y="500" width="706" height="84" rx="14"/>
    <text class="decal__url" x="470" y="558" text-anchor="middle"
          textLength="605" lengthAdjust="spacingAndGlyphs">www.marisoldeane.com</text>

    <text class="decal__tagline" x="470" y="640" text-anchor="middle"
          textLength="504" lengthAdjust="spacingAndGlyphs">World Renowned for Over 45 Years.</text>
  </svg>
</main>
</body>
</html>
```